FR banner

we need a banner design (36"x120" horizontal) that will be displayed on a local high school baseball field. My company ( Crestwell Prints Co) has been producing signage for the Fernmoor Ridge community since 2009. We would like to communicate that we do more than banners. The final design should include the slogan "Signs Shirts Swag" and our Logo.

Target Market(s)

companies, teams, events, shirt and other marketing items.

Industry/Entity Type

Sign, Print,

Font styles to use
Sans Serif

Requirements
Should not have
• no baseball content.

```html
<!DOCTYPE html>
<html lang="en">
<head>
<meta charset="utf-8">
<title>Crestwell Prints Co – Signs Shirts Swag Banner</title>
<link rel="stylesheet" href="https://fonts.googleapis.com/css2?family=Anton&family=Nunito+Sans:wght@800&display=swap">
<style>
  :root {
    --stage: #404040;
    --purple: #382d7b;
    --sky-band: #c9e6f0;
    --orange: #f15a3a;
    --mint: #c8e8e3;
    --green: #a2d28f;
    --yellow: #fff38a;
    --pink: #e95a78;
    --blue: #92c1ea;
    --white: #ffffff;
  }
  html, body {
    margin: 0;
    padding: 0;
    width: 1200px;
    height: 1200px;
    overflow: hidden;
    background: var(--stage);
  }
  .canvas { display: block; width: 1200px; height: 1200px; }
  .banner-body { fill: var(--purple); }
  .header-band, .drip { fill: var(--sky-band); }
  .drip-line { stroke: var(--sky-band); stroke-width: 2; fill: none; }
  .brand-name {
    font-family: "Anton", "Arial Narrow", sans-serif;
    font-size: 40px;
    fill: var(--purple);
    letter-spacing: 1px;
  }
  .slogan {
    font-family: "Anton", "Arial Narrow", sans-serif;
    font-size: 88px;
  }
  .slogan--warm { fill: var(--orange); }
  .slogan--cool { fill: var(--mint); }
  .product-dot--ring { fill: none; stroke-width: 4; }
  .icon {
    fill: none;
    stroke-width: 2;
    stroke-linecap: round;
    stroke-linejoin: round;
  }
  .icon--dark { stroke: var(--purple); }
  .icon--green { stroke: var(--green); }
  .icon--mint { stroke: var(--mint); }
  .icon--yellow { stroke: var(--yellow); }
  .website {
    font-family: "Nunito Sans", "Helvetica", sans-serif;
    font-weight: 800;
    font-size: 21px;
    fill: var(--white);
  }
</style>
</head>
<body>
<svg class="canvas" viewBox="0 0 1200 1200" xmlns="http://www.w3.org/2000/svg" role="img" aria-label="Crestwell Prints Co horizontal banner: Signs Shirts Swag">
  <g class="banner" transform="translate(50 435)">
    <rect class="banner-body" x="0" y="0" width="1100" height="330"/>
    <rect class="header-band" x="0" y="0" width="250" height="330"/>

    <path class="drip" d="M249 112 Q249 164 304 164 L304 166 Q249 166 249 218 Z"/>
    <line class="drip-line" x1="302" y1="165" x2="318" y2="165"/>
    <polygon class="drip" points="325,165 319,167.5 319,173.5 315,168.5 309,170.5 312.5,165 309,159.5 315,161.5 319,156.5 319,162.5"/>

    <g class="brand">
      <text class="brand-name" x="125" y="158" text-anchor="middle">CRESTWELL</text>
      <text class="brand-name" x="125" y="204" text-anchor="middle">PRINTS CO</text>
    </g>

    <g class="slogan-stack">
      <text class="slogan slogan--warm" x="345" y="112" textLength="150" lengthAdjust="spacingAndGlyphs">SIGNS</text>
      <text class="slogan slogan--cool" x="345" y="202" textLength="178" lengthAdjust="spacingAndGlyphs">SHIRTS</text>
      <text class="slogan slogan--warm" x="345" y="292" textLength="136" lengthAdjust="spacingAndGlyphs">SWAG</text>
    </g>

    <g class="product-grid">
      <!-- Row 1 -->
      <g transform="translate(585 73)">
        <circle class="product-dot product-dot--ring" r="40" stroke="var(--green)"/>
        <g class="icon icon--mint" role="img" aria-label="Notebook">
          <rect x="-13" y="-17" width="24" height="34" rx="2"/>
          <path d="M-1 -7 l-4 -4 a2.5 2.5 0 0 1 4 -2 a2.5 2.5 0 0 1 4 2 Z"/>
          <line x1="-7" y1="10" x2="5" y2="10"/>
          <line x1="15" y1="-14" x2="15" y2="14"/>
        </g>
      </g>
      <g transform="translate(677 73)">
        <circle class="product-dot" r="42" fill="var(--yellow)"/>
        <g class="icon icon--dark" role="img" aria-label="Sign stand">
          <rect x="-12" y="-22" width="24" height="30"/>
          <polyline points="-8,0 -2,-9 4,0"/>
          <line x1="-8" y1="4" x2="8" y2="4"/>
          <line x1="0" y1="8" x2="0" y2="17"/>
          <line x1="-18" y1="17" x2="18" y2="17"/>
        </g>
      </g>
      <g transform="translate(769 73)">
        <circle class="product-dot product-dot--ring" r="40" stroke="var(--pink)"/>
        <g class="icon icon--green" role="img" aria-label="Water bottle">
          <rect x="-5" y="-22" width="10" height="6" rx="1"/>
          <rect x="-9" y="-16" width="18" height="38" rx="4"/>
          <line x1="-3" y1="2" x2="3" y2="2"/>
          <line x1="-3" y1="8" x2="3" y2="8"/>
          <line x1="-3" y1="14" x2="3" y2="14"/>
        </g>
      </g>
      <!-- Row 2 -->
      <g transform="translate(585 165)">
        <circle class="product-dot" r="42" fill="var(--blue)"/>
        <g class="icon icon--dark" role="img" aria-label="Keychain">
          <circle cx="0" cy="-20" r="5"/>
          <line x1="0" y1="-15" x2="0" y2="-8"/>
          <rect x="-13" y="-8" width="26" height="28" rx="3"/>
          <polyline points="-8,14 -2,5 3,11 6,8 9,14"/>
        </g>
      </g>
      <g transform="translate(677 165)">
        <circle class="product-dot" r="42" fill="var(--green)"/>
        <g class="icon icon--dark" role="img" aria-label="Cap">
          <path d="M-17 6 Q-17 -16 0 -16 Q17 -16 17 6 Z"/>
          <ellipse cx="0" cy="11" rx="22" ry="6"/>
          <circle cx="0" cy="-18" r="2"/>
        </g>
      </g>
      <g transform="translate(769 165)">
        <circle class="product-dot" r="42" fill="var(--blue)"/>
        <g class="icon icon--dark" role="img" aria-label="Backpack">
          <path d="M-5 -16 v-5 h10 v5"/>
          <rect x="-14" y="-16" width="28" height="36" rx="7"/>
          <rect x="-9" y="6" width="18" height="10" rx="2"/>
          <line x1="-14" y1="0" x2="14" y2="0"/>
        </g>
      </g>
      <!-- Row 3 -->
      <g transform="translate(585 257)">
        <circle class="product-dot" r="42" fill="var(--green)"/>
        <g class="icon icon--dark" role="img" aria-label="T-shirt">
          <path d="M-7 -18 L-20 -11 L-15 -2 L-11 -5 L-11 18 L11 18 L11 -5 L15 -2 L20 -11 L7 -18 Q0 -12 -7 -18 Z"/>
          <rect x="-5" y="-3" width="10" height="10"/>
        </g>
      </g>
      <g transform="translate(677 257)">
        <circle class="product-dot product-dot--ring" r="40" stroke="var(--blue)"/>
        <g class="icon icon--yellow" role="img" aria-label="Pen">
          <g transform="rotate(-45)">
            <rect x="-4" y="-20" width="8" height="30" rx="2"/>
            <path d="M-4 10 L0 20 L4 10"/>
            <line x1="-4" y1="-12" x2="4" y2="-12"/>
          </g>
        </g>
      </g>
      <g transform="translate(769 257)">
        <circle class="product-dot" r="42" fill="var(--pink)"/>
        <g class="icon icon--mint" role="img" aria-label="Mug">
          <rect x="-16" y="-15" width="26" height="30" rx="2"/>
          <path d="M10 -8 h4 a7 7 0 0 1 0 14 h-4"/>
          <path d="M-3 2 l-4 -4 a2.5 2.5 0 0 1 4 -2 a2.5 2.5 0 0 1 4 2 Z"/>
        </g>
      </g>
    </g>

    <text class="website" x="955" y="172" text-anchor="middle">www.crestwellprints.com</text>
  </g>
</svg>
</body>
</html>
```